Stationary/business card/envelope design for Ravenhill Dentalcare

We are located in the foothills of the sierra nevada mountains. We are looking for a beautiful classy modern stationary. We need evelopes and business card design all to flow seamlessly. Envelope design.

Additional office address 4816 Orchard Crest Rd., Suite B, Auburn, CA 95604 Phone: pending Fax: pending.

3 different Drs on each business card:
Marla J. Whitcombe, DDS
Tessa R. Whitcombe, DDS
Rosalind P. Haverty, DDS

Target Market(s)

Dental patients

Industry/Entity Type

Dental

Contact Information for Business Card

Two sided. See example.

Font styles to use
Sans Serif

Requirements
Must have
• One sided business cards. Need envelope design.
Colors should match existing logo.

Marla J. Whitcombe, DDS
Tessa R. Whitcombe, DDS
Rosalind P. Haverty, DDS

```html
<!DOCTYPE html>
<html lang="en">
<head>
<meta charset="utf-8">
<title>Ravenhill Dentalcare Stationery</title>
<link href="https://fonts.googleapis.com/css2?family=Lato:wght@300;400;700;900&family=Roboto+Condensed:wght@300;400&display=swap" rel="stylesheet">
<style>
  :root{
    --bg:#d9e4ef;
    --paper:#ffffff;
    --sky:#25b4dc;
    --pine:#17702f;
    --ink:#5a5a5a;
    --ink-dark:#4a4a4a;
  }
  *{margin:0;padding:0;box-sizing:border-box}
  html,body{width:1200px;height:831px;overflow:hidden;background:var(--bg)}
  body{position:relative;font-family:'Lato',sans-serif;color:var(--ink)}
  .sheet{position:absolute;background:var(--paper);box-shadow:0 4px 10px rgba(40,60,90,.35);overflow:hidden}
  .wave{position:absolute;left:0;bottom:0;width:100%;display:block}

  .brand{position:absolute;display:flex;align-items:center;gap:5px;color:var(--pine);font-family:'Lato',sans-serif;font-weight:700;line-height:1.1}
  .brand .dot{border-radius:50%;background:var(--sky);flex:none}

  /* Letterhead */
  .letterhead{left:116px;top:111px;width:431px;height:609px}
  .letterhead .brand{left:40px;top:40px;font-size:14px;width:120px}
  .letterhead .brand .dot{width:18px;height:18px}
  .contact{position:absolute;left:282px;top:31px;font-size:8.3px;line-height:11.5px;color:var(--ink)}
  .contact .addr{margin-bottom:4px}
  .contact li{list-style:none;display:flex;align-items:center;gap:8px;height:11.2px}
  .contact svg{width:7px;height:7px;flex:none}
  .letter{position:absolute;left:41px;top:208px;width:350px}
  .letter .date{font-size:10px;font-weight:300;color:var(--ink)}
  .letter .recipient{font-size:16px;font-weight:900;color:var(--ink-dark);margin-top:5px;letter-spacing:.2px}
  .letter .role{font-size:10px;font-weight:300;margin-top:2px}
  .letter .body{margin-top:26px;font-family:'Roboto Condensed',sans-serif;font-weight:300;font-size:8.4px;line-height:15px;text-align:justify;color:var(--ink-dark)}
  .letter .body p{margin-bottom:15px}
  .letter .closing{font-family:'Roboto Condensed',sans-serif;font-weight:300;font-size:9.5px;margin-top:25px;color:var(--ink-dark)}
  .signature{width:46px;height:30px;margin-top:10px;background:linear-gradient(135deg,rgba(23,112,47,.15),rgba(23,112,47,.35));border-radius:3px}

  /* Business card */
  .card{left:635px;top:112px;width:183px;height:105px}
  .card .brand{right:8px;top:14px;font-size:6px;width:62px;justify-content:flex-end;text-align:right}
  .card .brand .dot{width:9px;height:9px}
  .card .name{position:absolute;left:11px;top:46px;font-size:6.4px;font-weight:700;color:var(--pine)}
  .card .title{position:absolute;left:11px;top:54px;font-size:4.3px;color:var(--ink)}
  .card .rule{position:absolute;left:11px;right:11px;top:63px;border-top:.6px solid var(--pine)}
  .card .details{position:absolute;left:11px;top:67px;font-size:3.9px;line-height:6px}
  .card .details li{list-style:none;display:flex;align-items:center;gap:4px}
  .card .details svg{width:4px;height:4px}
  .card .address{position:absolute;right:11px;top:78px;font-size:3.9px;line-height:6.2px;text-align:right}

  /* Appointment card */
  .appt{left:904px;top:111px;width:182px;height:104px}
  .appt .brand{left:9px;top:16px;font-size:6px;width:60px}
  .appt .brand .dot{width:9px;height:9px}
  .appt .lines{position:absolute;right:10px;top:8px;font-size:3.5px;line-height:6px;text-align:right;color:var(--ink)}
  .appt .lines b{font-weight:400;color:var(--sky)}
  .appt .name{position:absolute;right:10px;top:29px;font-size:7px;font-weight:700;color:var(--pine)}
  .appt .title{position:absolute;right:10px;top:39px;font-size:4.3px}
  .appt .rule{position:absolute;left:9px;right:10px;top:50px;border-top:.6px solid #9a9a9a}
  .appt .next{position:absolute;left:9px;top:55px;display:flex;gap:5px;align-items:center;font-size:3.9px;color:#888}
  .appt .next strong{font-size:5.4px;font-weight:400;color:var(--sky);margin-right:2px}
  .appt .next span::before{content:"";display:inline-block;width:3px;height:3px;border:.5px solid var(--sky);border-radius:50%;margin-right:1.5px;vertical-align:middle}
  .appt .field{position:absolute;left:79px;font-size:5.2px;color:var(--sky);display:flex;align-items:flex-end;gap:3px}
  .appt .field i{display:block;width:68px;border-bottom:.5px solid #888;height:4px}
  .appt .notice{position:absolute;left:0;right:0;bottom:0;height:11px;background:var(--sky);color:#fff;font-size:3.6px;letter-spacing:.8px;display:flex;align-items:center;justify-content:center}

  /* Envelopes */
  .envelope-back{left:635px;top:248px;width:451px;height:226px}
  .flap{position:absolute;left:0;top:0;width:451px;height:66px;display:block}
  .envelope-front{left:635px;top:494px;width:451px;height:226px}
  .envelope-front .brand{left:42px;top:55px;font-size:14px;width:120px}
  .envelope-front .brand .dot{width:18px;height:18px}
  .return{position:absolute;left:45px;top:161px;padding-left:9px;border-left:1.2px solid var(--pine);font-size:8px;line-height:10.8px;font-weight:300}
</style>
</head>
<body>

<svg width="0" height="0" style="position:absolute" aria-hidden="true">
  <defs>
    <symbol id="i-phone" viewBox="0 0 10 10"><path d="M2 1l2 2-1 1.3c.6 1.2 1.5 2.1 2.7 2.7L7 6l2 2-1.2 1.4C4.5 9 1 5.5.6 2.2Z" fill="#25b4dc"/></symbol>
    <symbol id="i-fax" viewBox="0 0 10 10"><rect x="2.5" y="1" width="5" height="3" fill="#25b4dc"/><rect x="1" y="4" width="8" height="4" rx="1" fill="#25b4dc"/><rect x="3" y="7" width="4" height="2.5" fill="#fff" stroke="#25b4dc" stroke-width=".7"/></symbol>
    <symbol id="i-mail" viewBox="0 0 10 10"><rect x="1" y="2.5" width="8" height="5.5" fill="#25b4dc"/><path d="M1 2.5l4 3 4-3" fill="none" stroke="#fff" stroke-width=".7"/></symbol>
    <symbol id="i-web" viewBox="0 0 10 10"><circle cx="5" cy="5" r="4" fill="none" stroke="#25b4dc" stroke-width=".9"/><path d="M1 5h8M5 1c-2 2.5-2 5.5 0 8M5 1c2 2.5 2 5.5 0 8" fill="none" stroke="#25b4dc" stroke-width=".6"/></symbol>
  </defs>
</svg>

<!-- Letterhead -->
<section class="sheet letterhead">
  <div class="brand"><span class="dot"></span><span>Ravenhill Dentalcare</span></div>
  <div class="contact">
    <p class="addr">4816 Orchard Crest Rd.,<br>Suite B, Auburn, CA 95604</p>
    <ul>
      <li><svg><use href="#i-phone"/></svg>916-555-0142</li>
      <li><svg><use href="#i-fax"/></svg>916-555-0178</li>
      <li><svg><use href="#i-mail"/></svg>ravenhilldentalcare@mailbox.com</li>
      <li><svg><use href="#i-web"/></svg>www.ravenhilldentalcare.com</li>
    </ul>
  </div>
  <div class="letter">
    <p class="date">01 December, 2021</p>
    <h1 class="recipient">DANIEL CRANE</h1>
    <p class="role">Cheif Executive Officer</p>
    <div class="body">
      <p>Contrary to popular belief, Lorem Ipsum is not simply random text. It has roots in a piece of classical Latin literature from 45 BC, making it over 2000 years old. Howard Pelling, a Latin professor at Larchmont College in Virginia, looked up one of the more obscure Latin words, consectetur.</p>
      <p>Lorem Ipsum comes from sections 1.10.32 and 1.10.33 of "de Finibus Bonorum et Malorum" (The Extremes of Good and Evil) by Aurelio Vanti, written in 45 BC. This book is a treatise on the theory of ethics, very popular during the Renaissance. The first line of Lorem Ipsum.</p>
      <p>The standard chunk of Lorem Ipsum used since the 1500s is reproduced below for those interested.</p>
    </div>
    <p class="closing">Best Regards</p>
    <div class="signature" role="img" aria-label="Handwritten signature"></div>
  </div>
  <svg class="wave" viewBox="0 0 431 38" height="38" preserveAspectRatio="none">
    <path d="M0 27 C70 14 170 14 270 22 C350 28 400 24 431 13 V38 H0Z" fill="var(--sky)"/>
    <path d="M16 13 C100 -1 190 4 280 12 C340 17 385 17 417 14 C380 22 320 22 260 17 C180 10 90 5 16 13Z" fill="var(--pine)"/>
  </svg>
</section>

<!-- Business card -->
<section class="sheet card">
  <div class="brand"><span>Ravenhill Dentalcare</span><span class="dot"></span></div>
  <p class="name">Marla J. Whitcombe, DDS</p>
  <p class="title">President &amp; CEO</p>
  <div class="rule"></div>
  <ul class="details">
    <li><svg><use href="#i-phone"/></svg>916-555-0142</li>
    <li><svg><use href="#i-fax"/></svg>916-555-0178</li>
    <li><svg><use href="#i-mail"/></svg>ravenhilldentalcare@mailbox.com</li>
    <li><svg><use href="#i-web"/></svg>www.ravenhilldentalcare.com</li>
  </ul>
  <p class="address">4816 Orchard Crest Rd.,<br>Suite B, Auburn, CA 95604</p>
  <svg class="wave" viewBox="0 0 183 12" height="12" preserveAspectRatio="none">
    <path d="M0 8 C40 2 90 4 130 7 C160 9 175 7 183 3 V12 H0Z" fill="var(--sky)"/>
    <path d="M8 4 C50 -1 100 3 140 5 C160 6 170 6 178 5 C160 8 140 8 120 6 C80 3 40 2 8 4Z" fill="var(--pine)"/>
  </svg>
</section>

<!-- Appointment card -->
<section class="sheet appt">
  <div class="brand"><span class="dot"></span><span>Ravenhill Dentalcare</span></div>
  <p class="lines"><b>Office:</b> (916) 555-0142<br><b>Fax:</b> (916) 555-0178</p>
  <p class="name">Marla J. Whitcombe, DDS</p>
  <p class="title">President &amp; CEO</p>
  <div class="rule"></div>
  <div class="next"><strong>NEXT APPOINTMENT:</strong><span>Mon</span><span>Tue</span><span>Wed</span><span>Thur</span><span>Fri</span></div>
  <div class="field" style="top:68px">Date: <i></i></div>
  <div class="field" style="top:78px">Time: <i></i></div>
  <div class="notice">IF UNABLE TO KEEP APPOINTMENT, KINDLY GIVE 24 HOUR NOTICE</div>
</section>

<!-- Envelope back -->
<section class="sheet envelope-back">
  <svg class="flap" viewBox="0 0 451 66">
    <path d="M0 0 H451 L446 40 Q443 66 417 66 H34 Q8 66 5 40 Z" fill="var(--sky)"/>
  </svg>
</section>

<!-- Envelope front -->
<section class="sheet envelope-front">
  <div class="brand"><span class="dot"></span><span>Ravenhill Dentalcare</span></div>
  <p class="return">4816 Orchard Crest Rd.,<br>Suite B, Auburn, CA 95604</p>
  <svg class="wave" viewBox="0 0 451 30" height="30" preserveAspectRatio="none">
    <path d="M0 20 C80 8 180 10 290 17 C370 22 420 19 451 12 V30 H0Z" fill="var(--sky)"/>
    <path d="M16 12 C110 0 210 4 310 10 C370 13 410 13 436 11 C400 17 340 17 280 13 C190 7 100 5 16 12Z" fill="var(--pine)"/>
  </svg>
</section>

</body>
</html>
```